AMAZING FLYERS, POSTCARDS, AND MARKETING!!!! - Northgable Shingle & Eave Works, LLC

This project will be for Northgable Shingle & Eave Works, LLC. The flyers and postcards will be used to saturate the Alaska market with our services, and get our name and logo out there for people to remember. We plan to send the flyers and postcards out in a broad scale (both door to door and mail out). We want to send out flyers to realty and property management businesses to introduce our roofing company, and to advertise our services. We would also like to have another version, or the ability to edit the text of the final product to send out the same materials to residential clients (homeowners) by just changing the text slightly to better fit that market.
We have a logo, but need something put together that we can tri-fold and mail out to potential clients. We are planning to do some postcards as well. We would like the option to mail them or bring them to people in person.
We are a locally owned roofing and repair company in Alaska. We would like something professional that will capture their attention and show the potential of working with our company. I included some detailed information about our company and some pictures below of our work trailer and a before/after on a recent project. I also attached our logo files. Please go through the attached data and let us know what you come up with to stir up the marketing aspect of our company. Thank you for your time and consideration.

Project Deadline Extended
Reason: Allowing additional time for designers to submit/resubmit their flyer/postcard ideas based on inquiries and feedback.

Target Market(s)

1.) Homeowners are the first target market.
2.)Realtors and Property Management companies are the second market

Industry/Entity Type

Marketing

Contact Information for Business Card

Include the logo and contact information for our company. These business cards will be for the Owner, Harold Vemstrup, II.
There is also a Co-Owner, Wanda Vemstrup, so we will need the ability to print business cards for each owner. Need to be able to change the title/name and phone number for Wanda's contact information please. Contact information, license #, and logo information on one side of the card. Please tell the potential client a little about us on the back of the card by utilizing the attached information.

Requirements
Must have
• Pertinent information about our company and listed in the company information attachment. Attention getting details and design work. Professional in appearance and unique to our company to set us above the general advertisers in this industry.
Nice to have
• Something that sets our flyers apart from the ones people get every day. We want to rise above normal with our advertising.
Should not have
• Nothing plain and boring.

```html
<!DOCTYPE html>
<html lang="en">
<head>
<meta charset="utf-8">
<title>Northgable Shingle &amp; Eave Works, LLC — Tri-fold Brochure</title>
<link rel="stylesheet" href="https://fonts.googleapis.com/css2?family=Archivo:wght@800&family=Lato:wght@400;900&family=Marcellus&family=Michroma&display=swap">
<style>
  :root {
    --backdrop: #e9e6e2;
    --paper: #ffffff;
    --paper-shade: #d9d9d9;
    --ink: #111111;
    --band: #0b0b0b;
    --silver: #bdbdbd;
    --roof-a: #8d9196;
    --roof-b: #5d6166;
    --house-sky: #dfe6ec;
    --house-lawn: #5f8a3a;
    --trailer: #1c1c1c;
  }
  * { box-sizing: border-box; margin: 0; padding: 0; }
  html, body { width: 1200px; height: 907px; overflow: hidden; }
  body { background: var(--backdrop); position: relative; font-family: "Lato", Arial, sans-serif; color: var(--ink); }

  .brochure {
    position: absolute; left: 80px; top: 80px; width: 1040px; height: 745px;
    background: linear-gradient(90deg, var(--paper) 0%, #f1f1f1 30%, var(--paper-shade) 34%, #f4f4f4 40%, var(--paper) 66%, #e6e6e6 67%, var(--paper) 70%);
    box-shadow: 0 6px 18px rgba(0,0,0,.25);
    overflow: hidden;
  }
  .brochure__shapes { position: absolute; inset: 0; }

  .about { position: absolute; left: 36px; top: 40px; width: 310px; }
  .about__title { font-family: "Michroma", "Arial Black", sans-serif; font-size: 25px; letter-spacing: 1px; text-align: center; margin-left: 40px; width: 240px; margin-bottom: 22px; }
  .about__body { font-size: 11.3px; line-height: 14.6px; text-align: justify; }

  .contact { position: absolute; left: 370px; top: 340px; width: 300px; }
  .contact__phone { display: flex; align-items: center; gap: 4px; margin-left: 33px; font-family: "Archivo", Arial, sans-serif; font-size: 26px; }
  .contact__line { display: flex; align-items: center; gap: 6px; font-size: 12.5px; margin-top: 10px; }
  .contact__line--mail { margin-left: 35px; margin-top: 14px; }
  .contact__line--web { margin-left: 5px; }

  .brand { position: absolute; left: 720px; top: 30px; width: 300px; text-align: center; }
  .brand__name { display: flex; align-items: center; justify-content: center; gap: 10px; font-family: "Lato", Arial, sans-serif; font-weight: 900; font-size: 22px; line-height: 26px; text-transform: uppercase; height: 150px; }
  .brand__mark { width: 16px; height: 16px; background: var(--ink); flex: none; }
  .brand__headline { font-family: "Archivo", Arial, sans-serif; font-size: 26px; margin-top: 22px; letter-spacing: .5px; }
  .brand__tagline { font-family: "Marcellus", Georgia, serif; font-size: 27px; margin-top: 2px; }
</style>
</head>
<body>
  <main class="brochure">
    <svg class="brochure__shapes" width="1040" height="745" viewBox="0 0 1040 745" aria-hidden="false">
      <defs>
        <linearGradient id="roofFill" x1="0" y1="0" x2="1" y2="1">
          <stop offset="0" stop-color="#7c9a5a"/>
          <stop offset=".35" stop-color="var(--roof-a)"/>
          <stop offset="1" stop-color="var(--roof-b)"/>
        </linearGradient>
        <linearGradient id="houseFill" x1="0" y1="0" x2="0" y2="1">
          <stop offset="0" stop-color="var(--house-sky)"/>
          <stop offset=".45" stop-color="#a9adb2"/>
          <stop offset=".7" stop-color="#4f5357"/>
          <stop offset="1" stop-color="var(--house-lawn)"/>
        </linearGradient>
      </defs>

      <!-- top black wedge of centre panel -->
      <polygon class="band band--wedge" points="365,0 695,0 695,265 668,252" fill="var(--band)"/>

      <!-- trailer photo -->
      <rect class="photo photo--trailer" x="352" y="140" width="318" height="165" rx="4" fill="var(--trailer)" role="img" aria-label="Photo of the company work trailer with ladders on its roof rack"/>

      <!-- lower-left roof photo with bands -->
      <polygon class="band" points="0,455 128,455 372,672 372,688 120,472 0,472" fill="var(--band)"/>
      <polygon class="band band--silver" points="0,472 120,472 372,688 372,700 112,482 0,482" fill="var(--silver)"/>
      <polygon class="photo photo--roof" points="0,482 112,482 372,700 372,745 0,745" fill="url(#roofFill)" role="img" aria-label="Photo of a newly shingled grey roof with vents"/>

      <!-- right-panel horizontal band and big diagonal band -->
      <rect class="band" x="695" y="262" width="345" height="18" fill="var(--band)"/>
      <polygon class="band" points="668,252 695,262 1040,262 1040,290 700,290 372,745 325,745" fill="var(--band)"/>
      <polygon class="band band--silver" points="700,290 712,290 384,745 372,745" fill="var(--silver)"/>

      <!-- house photo -->
      <polygon class="photo photo--house" points="712,290 1040,290 1040,745 384,745" fill="url(#houseFill)" role="img" aria-label="Photo of a finished home with a new dark roof, garage and driveway"/>
    </svg>

    <section class="about">
      <h2 class="about__title">ABOUT US</h2>
      <p class="about__body">Usu postea temporibus ne, quo at iusto atomorum persecuti, in viderer disputationi eum. Exerci dissentiet cu usu, postea consulatu incidérint vel cu. Et nihil tritani per, id ius ignota inciderint. Discere ancillae lobortis ius ut.<br>Volumus pertinacia sed an, at vis commune delicata incorrupte. No modus graeci docendi his, ea mnesarchum disputationi ius. Mucius ponderum verterem pro at, vix cu laoreet omnesque. Ex dicat iudico noster eum, ut vix laudem veritus, sea ei consul officiis dissentias. Brute nullam gloriatur ut eos, ne vim sumo oblique.<br>Suas graeci sea id, sea cibo propriae no. Malis vivendum percipitur mei ea, vel tation luptatum ne. Id pro stet legere volutpat, probo concludaturque vel an, mei essent perfecto et. No sea oratio probatus, an facilis officiis eum, te eos eloquentiam efficiantur. Te error consectetuer usu, stet dictas consectetuer ius at, mucius reformidans qui ei. Error tacimates pri cu, usu ne vidisse prodesset, nam cu principes intellegam complectitur.</p>
    </section>

    <section class="contact">
      <p class="contact__phone">
        <svg width="20" height="20" viewBox="0 0 20 20" aria-hidden="true"><rect x="0" y="0" width="20" height="20" rx="4" fill="var(--ink)"/><path d="M6 4c1 0 2 3 1.5 3.5L6.5 8.5c.8 2 2.5 3.7 4.5 4.5l1-1c.5-.5 3.5.5 3.5 1.5 0 1-1.5 2.5-2.5 2.5C8 16 4 12 4 6.5 4 5.5 5 4 6 4z" fill="#fff"/></svg>
        0123456789
      </p>
      <p class="contact__line contact__line--mail">
        <svg width="13" height="10" viewBox="0 0 13 10" aria-hidden="true"><rect x=".5" y=".5" width="12" height="9" fill="none" stroke="var(--ink)"/><path d="M.5 .5l6 5 6-5" fill="none" stroke="var(--ink)"/></svg>
        www.company@mail.com
      </p>
      <p class="contact__line contact__line--web">
        <svg width="12" height="12" viewBox="0 0 12 12" aria-hidden="true"><circle cx="6" cy="6" r="5.5" fill="none" stroke="var(--ink)"/><ellipse cx="6" cy="6" rx="2.3" ry="5.5" fill="none" stroke="var(--ink)"/><path d="M.5 6h11" stroke="var(--ink)"/></svg>
        www.companywebsite .com
      </p>
    </section>

    <header class="brand">
      <p class="brand__name"><span class="brand__mark"></span><span>Northgable Shingle<br>&amp; Eave Works, LLC</span></p>
      <h1 class="brand__headline">LOREM IPSUM</h1>
      <p class="brand__tagline">DOLOR SIT AMET</p>
    </header>
  </main>
</body>
</html>
```